Brintell's Business Card

I need some designs for a new business card including the new logo attached. An old example of our business card is also attached to show all the data that should be included on the new design.
**I added some more examples someone had mocked up**

Contact Information for Business Card

Should include all info on other examples uploaded.

```html
<!DOCTYPE html>
<html lang="en">
<head>
<meta charset="utf-8">
<title>Brintell's Business Cards</title>
<link rel="stylesheet" href="https://fonts.googleapis.com/css2?family=Montserrat:wght@500;600;700&family=PT+Sans:ital,wght@1,400&display=swap">
<style>
  :root {
    --blue: #3f6fb0;
    --blue-light: #c3d8eb;
    --navy: #2b5597;
    --red: #d0262f;
    --white: #ffffff;
    --backdrop: #ebe7e0;
  }
  html, body {
    margin: 0;
    width: 1200px;
    height: 1200px;
    overflow: hidden;
    background: var(--backdrop);
  }
  .sheet { position: relative; width: 1200px; height: 1200px; }
  .card {
    position: absolute;
    width: 620px;
    height: 355px;
    box-shadow: 0 6px 18px rgba(0,0,0,0.18);
    display: block;
  }
  .card--dale { left: 70px; top: 35px; }
  .card--evan { left: 510px; top: 420px; }
  .card--back { left: 110px; top: 805px; }
  .brand-name { font-family: "Montserrat", sans-serif; font-weight: 700; fill: var(--navy); }
  .person-name { font-family: "Montserrat", sans-serif; font-weight: 700; fill: var(--white); letter-spacing: 1px; }
  .contact { font-family: "Montserrat", sans-serif; font-weight: 500; fill: var(--navy); }
  .tagline { font-family: "PT Sans", sans-serif; font-style: italic; fill: var(--white); }
  .band-text { font-family: "Montserrat", sans-serif; font-weight: 600; fill: var(--white); }
  .call-text { font-family: "Montserrat", sans-serif; font-weight: 500; fill: var(--navy); }
  .icon { fill: none; stroke: var(--navy); stroke-width: 2; stroke-linejoin: round; stroke-linecap: round; }
</style>
</head>
<body>
<main class="sheet">

  <svg class="card card--dale" viewBox="0 0 620 355" role="group" aria-label="Business card for Dale Brintell">
    <rect width="620" height="355" fill="var(--white)"/>
    <path d="M0 185 Q300 160 620 172 L620 355 L0 355 Z" fill="var(--blue-light)"/>
    <rect y="128" width="620" height="38" fill="var(--blue)"/>
    <path d="M0 290 Q360 300 620 238 L620 355 L0 355 Z" fill="var(--blue)"/>
    <circle cx="62" cy="72" r="20" fill="var(--red)"/>
    <text class="brand-name" x="94" y="88" font-size="44">Brintell's</text>
    <text class="person-name" x="48" y="156" font-size="24">DALE BRINTELL</text>
    <path class="icon" d="M52 210 l6 -3 l5 8 l-4 3 q3 6 9 9 l3 -4 l8 5 l-3 6 q-18 -4 -24 -24 z"/>
    <text class="contact" x="92" y="228" font-size="21">555 - 014 - 3817</text>
    <rect class="icon" x="52" y="247" width="26" height="18"/>
    <path class="icon" d="M52 247 L65 258 L78 247"/>
    <text class="contact" x="92" y="263" font-size="21">hvacbrintell@example.com</text>
    <text class="tagline" x="330" y="330" font-size="22" text-anchor="middle">Licensed &amp; insured - Family owned &amp; operated</text>
  </svg>

  <svg class="card card--evan" viewBox="0 0 620 355" role="group" aria-label="Business card for Evan Brintell">
    <rect width="620" height="355" fill="var(--white)"/>
    <path d="M0 185 Q300 160 620 172 L620 355 L0 355 Z" fill="var(--blue-light)"/>
    <rect y="128" width="620" height="38" fill="var(--blue)"/>
    <path d="M0 290 Q360 300 620 238 L620 355 L0 355 Z" fill="var(--blue)"/>
    <circle cx="102" cy="72" r="20" fill="var(--red)"/>
    <text class="brand-name" x="134" y="88" font-size="44">Brintell's</text>
    <text class="person-name" x="60" y="156" font-size="24">EVAN BRINTELL</text>
    <path class="icon" d="M62 210 l6 -3 l5 8 l-4 3 q3 6 9 9 l3 -4 l8 5 l-3 6 q-18 -4 -24 -24 z"/>
    <text class="contact" x="102" y="228" font-size="21">555 - 014 - 6042</text>
    <rect class="icon" x="62" y="247" width="26" height="18"/>
    <path class="icon" d="M62 247 L75 258 L88 247"/>
    <text class="contact" x="102" y="263" font-size="21">hvacbrintell@example.com</text>
    <text class="tagline" x="340" y="330" font-size="22" text-anchor="middle">Licensed &amp; insured - Family owned &amp; operated</text>
  </svg>

  <svg class="card card--back" viewBox="0 0 620 355" role="group" aria-label="Back of Brintell's business card">
    <rect width="620" height="355" fill="var(--white)"/>
    <rect y="28" width="620" height="44" fill="var(--blue)"/>
    <text class="band-text" x="310" y="58" font-size="21" text-anchor="middle">Serves Millbrook, IA &amp; surrounding areas</text>
    <circle cx="190" cy="190" r="24" fill="var(--red)"/>
    <text class="brand-name" x="228" y="208" font-size="52">Brintell's</text>
    <path d="M0 262 Q320 286 620 256 L620 355 L0 355 Z" fill="var(--blue-light)"/>
    <path d="M0 310 Q320 318 620 292 L620 355 L0 355 Z" fill="var(--blue)"/>
    <text class="call-text" x="310" y="296" font-size="15" text-anchor="middle">Call today for all your HVAC, Refrigeration and Plumbing needs</text>
  </svg>

</main>
</body>
</html>
```